Tarek & Lubna's 50th Anniversary Celebration & Reunion

I need a flyer to send out via email and for posting on facebook to invite guests to a 50th wedding anniversary / family reunion.

Location is sunny La Jolla CA the Jewel of San Diego's Coast.

Week long daily activities starting Mon July 28-Aug 1st Friday, The event will be on Wednesday.
* Daily Catered Family Breakfast at the Marlow Hall of La Jolla
* Daily group activities including
*Exploring La Jolla Beaches & Ocean Cave Kayaking
*TideLand Private Behind the Scenes Tour
*World Famous Harbor Wild Park
*Sunset Balloon Ride
*Private Yatch on the Bay

Actual Anniversary event will take place Thursday December 28, 2013 at 5pm at the Marlow Hall.

There are many local hotels around the Marlow Hall. 4512 Pell Ave, La Jolla, CA 92037

Host is Remond and the entire Halabi Family. For questions, please email Remond@thegrovefeasts.com

Target Market(s)

all ages from 10 year olds to 70 year olds. Should appeal to all

Industry/Entity Type

Wedding

Font styles to use
Script

Colors

Designer to choose colors to be used in the design.

Requirements
Must have
• Fun graphics, including one with a stretch limo as there will be one available

Nice to have
• Logo for TideLand Inserting a picture of an actual wedding 50 years ago or so of the bride and groom. incorporating the limo cropped out of the picture attached would also be nice

```html
<!DOCTYPE html>
<html lang="en">
<head>
<meta charset="utf-8">
<title>Tarek &amp; Lubna – 50th Anniversary</title>
<link href="https://fonts.googleapis.com/css2?family=Cinzel:wght@400;700&family=Great+Vibes&display=swap" rel="stylesheet">
<style>
  :root {
    --sky-top: #d3e8e6;
    --sky-low: #e6f0ee;
    --limo: #2f3436;
    --road: #8c9494;
    --script-blue: #3c80d2;
    --ink-dark: #1d1d1d;
    --gold: #f5e31c;
    --white: #ffffff;
    --panel: rgba(120, 170, 170, 0.35);
    --banner: rgba(20, 20, 20, 0.78);
    --photo-light: #cfcfcf;
    --photo-dark: #3a3a3a;
    --logo-ink: #123a6b;
  }
  html, body {
    margin: 0;
    padding: 0;
    overflow: hidden;
    background: #ffffff;
  }
  .flyer {
    position: relative;
    width: 1200px;
    height: 849px;
    overflow: hidden;
  }
  .backdrop-scene {
    position: absolute;
    inset: 0;
    background:
      linear-gradient(to bottom,
        var(--sky-top) 0%,
        var(--sky-low) 60%,
        #9aa6a4 64%,
        var(--limo) 67%,
        #3d4345 80%,
        var(--limo) 86%,
        var(--road) 90%,
        #a3aaaa 100%);
  }
  .wedding-photo {
    position: absolute;
    left: 57px;
    top: 40px;
    width: 352px;
    height: 513px;
    border: 5px solid var(--white);
    background: linear-gradient(135deg, var(--photo-dark) 0%, #7a7a7a 40%, var(--photo-light) 60%, #6b6b6b 100%);
  }
  .event-date, .event-time {
    position: absolute;
    margin: 0;
    font-family: "Great Vibes", cursive;
    font-weight: 400;
    color: var(--script-blue);
    line-height: 1;
    white-space: nowrap;
  }
  .event-date { left: 458px; top: 38px; font-size: 62px; }
  .event-time { left: 512px; top: 90px; font-size: 62px; }
  .event-tagline {
    position: absolute;
    right: 22px;
    top: 138px;
    margin: 0;
    font-family: "Great Vibes", cursive;
    font-size: 23px;
    color: var(--ink-dark);
    white-space: nowrap;
  }
  .activity-panel {
    position: absolute;
    left: 482px;
    top: 182px;
    width: 703px;
    height: 346px;
    background: var(--panel);
  }
  .activity-list {
    list-style: none;
    margin: 0;
    padding: 14px 14px 0 0;
    text-align: right;
    font-family: "Cinzel", serif;
    font-size: 25px;
    line-height: 36.5px;
    color: var(--white);
    text-transform: lowercase;
    font-variant: small-caps;
  }
  .activity-list li::first-letter { text-transform: uppercase; }
  .anniversary-number {
    position: absolute;
    left: 52px;
    top: 468px;
    margin: 0;
    font-family: "Cinzel", serif;
    font-weight: 400;
    font-size: 172px;
    line-height: 1;
    color: var(--gold);
    letter-spacing: -4px;
  }
  .anniversary-word {
    position: absolute;
    left: 62px;
    top: 622px;
    margin: 0;
    font-family: "Cinzel", serif;
    font-weight: 400;
    font-size: 64px;
    line-height: 1;
    color: var(--gold);
  }
  .partner-mark {
    position: absolute;
    left: 137px;
    top: 700px;
    width: 228px;
    height: 135px;
    background: var(--white);
    display: flex;
    align-items: center;
    justify-content: center;
    gap: 10px;
  }
  .partner-dot {
    width: 22px;
    height: 22px;
    border-radius: 50%;
    background: var(--logo-ink);
  }
  .partner-name {
    font-family: "Cinzel", serif;
    font-weight: 700;
    font-size: 30px;
    color: var(--logo-ink);
  }
  .invite-banner {
    position: absolute;
    left: 437px;
    top: 768px;
    width: 711px;
    height: 59px;
    background: var(--banner);
    display: flex;
    align-items: center;
    justify-content: center;
  }
  .invite-banner p {
    margin: 0;
    font-family: "Cinzel", serif;
    font-size: 40px;
    color: var(--white);
    white-space: nowrap;
  }
</style>
</head>
<body>
<main class="flyer">
  <div class="backdrop-scene" role="img" aria-label="Black stretch limousine parked beside palm trees under a pale coastal sky"></div>

  <div class="wedding-photo" role="img" aria-label="Black and white wedding portrait of the bride and groom fifty years ago"></div>

  <h2 class="event-date">Monday 30th July 2014</h2>
  <h2 class="event-time">5pm at the Marlow Hall</h2>
  <p class="event-tagline">Sunny La Jolla CA the Jewel of San Diego's Coast.</p>

  <section class="activity-panel">
    <ul class="activity-list">
      <li>* Daily Catered Family Breakfast at the Marlow Hall</li>
      <li>of La Jolla</li>
      <li>* Daily group activities including</li>
      <li>*Exploring La Jolla Beaches &amp; Ocean Cave</li>
      <li>Kayaking</li>
      <li>*TideLand Private Behind the Scenes Tour</li>
      <li>*World Famous Harbor Wild Park</li>
      <li>*Sunset Balloon Ride</li>
      <li>*Private Yatch on the Bay</li>
    </ul>
  </section>

  <h1 class="anniversary-number">50TH</h1>
  <p class="anniversary-word">Anniversary</p>

  <div class="partner-mark">
    <span class="partner-dot"></span>
    <span class="partner-name">TideLand</span>
  </div>

  <div class="invite-banner">
    <p>Please come celebrate with us!</p>
  </div>
</main>
</body>
</html>
```